Volora Laundry and Dry Cleaning Poster

We need a Poster and Window Sticker for our Laundry and Dry cleaning shop (VOLORA LAUNDRY AND DRY CLEANING).
info we like on the design. Logo is included
Company Name: Volora Laundry and Dry Cleaning
Slogan: Always Fresh & Neat
Location: Kwentu-Dasor, Accra
Working Hours: Mon-Sat 8am to 5pm
Tel: +233 30 781 6242
email:info@voloralaundry.example
website: www.voloralaundry.example
fb: fb.com/voloralaundry

Target Market(s)

Laundry Shop

Colors
33a6d7
9bcb3b

```html
<!DOCTYPE html>
<html lang="en">
<head>
<meta charset="utf-8">
<title>Volora Laundry and Dry Cleaning – Poster and Window Sticker</title>
<link href="https://fonts.googleapis.com/css2?family=Open+Sans:wght@400;600;700;800&display=swap" rel="stylesheet">
<style>
  :root {
    --backdrop: #9fcdea;
    --white: #ffffff;
    --brand-blue: #1f8fd0;
    --deep-blue: #2a78c2;
    --sky-blue: #6cc0ec;
    --pale-blue: #d9eef9;
    --teal: #1dbb9c;
    --ink: #000000;
    --text-dark: #1b1b1b;
    --font: "Open Sans", Arial, sans-serif;
  }
  * { box-sizing: border-box; margin: 0; padding: 0; }
  html, body { width: 681px; height: 1200px; overflow: hidden; }
  body { background: var(--backdrop); font-family: var(--font); position: relative; }

  .side-label {
    position: absolute; color: var(--ink); font-weight: 800;
    transform: rotate(-90deg); transform-origin: center; white-space: nowrap;
  }
  .side-label--poster { font-size: 66px; left: -70px; top: 316px; width: 230px; text-align: center; letter-spacing: 1px; }
  .side-label--sticker { font-size: 44px; left: 32px; top: 920px; width: 300px; text-align: center; }

  .poster { position: absolute; left: 90px; top: 16px; width: 578px; height: 694px; background: var(--white); overflow: hidden; }
  .poster__waves { position: absolute; inset: 0; }

  .brand { position: absolute; text-align: left; }
  .brand__row { display: flex; align-items: center; gap: 8px; }
  .brand__dot { width: 58px; height: 58px; border-radius: 50%; background: var(--brand-blue); flex: none; }
  .brand__name { color: var(--brand-blue); font-weight: 700; font-size: 56px; line-height: 1; letter-spacing: -1px; }
  .brand__sub { color: var(--brand-blue); font-weight: 600; font-size: 10.5px; margin-left: 92px; margin-top: 2px; }
  .brand__slogan { color: var(--brand-blue); font-weight: 700; font-size: 17px; margin-left: 84px; line-height: 1.2; }
  .poster .brand { left: 145px; top: 22px; }
  .sticker .brand { left: 44px; top: 34px; transform: scale(0.86); transform-origin: left top; }

  .call-bubble { position: absolute; left: 60px; top: 104px; width: 170px; height: 150px; }
  .call-bubble__number {
    position: absolute; left: 78px; top: 182px; width: 134px; text-align: center;
    color: var(--white); font-weight: 700; font-size: 13px; white-space: nowrap;
  }

  .contact-card {
    position: absolute; left: 326px; top: 232px; width: 212px; height: 134px;
    background: var(--white); border-radius: 12px; box-shadow: 0 3px 8px rgba(0,0,0,.35);
    padding: 16px 0 0 14px;
  }
  .contact-line { display: flex; align-items: center; gap: 12px; font-size: 13px; color: var(--text-dark); height: 36px; white-space: nowrap; }
  .contact-line svg { flex: none; }

  .hours-card {
    position: absolute; width: 236px; height: 158px; background: var(--white);
    border-radius: 16px; box-shadow: 0 3px 8px rgba(0,0,0,.35); padding: 8px;
  }
  .poster .hours-card { left: 26px; top: 312px; }
  .hours-card__panel {
    height: 100%; border-radius: 12px; padding: 6px;
    background: linear-gradient(100deg, var(--deep-blue), var(--sky-blue) 55%, var(--deep-blue));
  }
  .hours-card__open { color: var(--white); font-weight: 700; font-size: 42px; text-align: center; line-height: 58px; }
  .hours-card__times { background: var(--white); border-radius: 10px; text-align: center; padding: 6px 0 4px; }
  .hours-card__days { color: var(--brand-blue); font-weight: 700; font-size: 18px; line-height: 1.3; }
  .hours-card__time { color: var(--teal); font-weight: 700; font-size: 19px; line-height: 1.4; }

  .laundry-art { position: absolute; left: 312px; top: 388px; width: 262px; height: 262px; }
  .web-address { position: absolute; font-weight: 700; color: var(--brand-blue); font-size: 18.5px; letter-spacing: 1.2px; white-space: nowrap; }
  .poster .web-address { left: 26px; top: 650px; }

  .sticker {
    position: absolute; left: 226px; top: 710px; width: 302px; height: 478px;
    background: var(--white); border-radius: 32px;
  }
  .sticker .hours-card { left: 30px; top: 140px; }
  .sticker .contact-list { position: absolute; left: 56px; top: 302px; }
  .sticker .contact-line { height: 36px; gap: 14px; font-size: 13px; }
  .sticker .contact-line:last-child { height: 30px; }
  .sticker .web-address { left: 0; width: 100%; text-align: center; top: 440px; font-size: 17.5px; letter-spacing: 1px; }
</style>
</head>
<body>

<div class="side-label side-label--poster">POSTER</div>
<div class="side-label side-label--sticker">Window Sticker</div>

<section class="poster">
  <svg class="poster__waves" viewBox="0 0 578 694" width="578" height="694" aria-hidden="true">
    <defs>
      <linearGradient id="fieldTint" x1="0" y1="0" x2="0" y2="1">
        <stop offset="0" stop-color="#c5e6f8"/>
        <stop offset="1" stop-color="#eef7fc"/>
      </linearGradient>
      <linearGradient id="bandBlue" x1="0" y1="0" x2="1" y2="0">
        <stop offset="0" stop-color="#2d7fc8"/>
        <stop offset=".45" stop-color="#7cc8ef"/>
        <stop offset=".75" stop-color="#3b8fd4"/>
        <stop offset="1" stop-color="#74c5ee"/>
      </linearGradient>
    </defs>
    <path d="M0,205 C110,285 230,280 340,205 C430,145 520,150 578,170 L578,694 L0,694 Z" fill="url(#fieldTint)"/>
    <path d="M0,200 C110,280 230,275 340,200 C430,140 520,145 578,165 L578,205 C520,180 440,180 360,230 C250,300 110,300 0,240 Z" fill="url(#bandBlue)"/>
    <path d="M0,580 C70,520 180,515 300,580 C380,625 440,640 578,640 L578,694 L0,694 Z" fill="var(--white)"/>
    <path d="M0,570 C70,510 180,505 300,570 C380,615 450,630 578,630 L578,650 C450,652 370,640 290,600 C180,545 80,560 0,625 Z" fill="url(#bandBlue)"/>
  </svg>

  <div class="brand">
    <div class="brand__row"><span class="brand__dot"></span><span class="brand__name">volora</span></div>
    <div class="brand__sub">LAUNDRY AND DRY CLEANING</div>
    <div class="brand__slogan">Always Fresh &amp; Neat</div>
  </div>

  <svg class="call-bubble" viewBox="0 0 170 150" aria-hidden="true">
    <defs>
      <radialGradient id="bubbleBlue" cx=".4" cy=".3" r=".8">
        <stop offset="0" stop-color="#7cc6ee"/>
        <stop offset="1" stop-color="#2a74c0"/>
      </radialGradient>
    </defs>
    <path d="M18,96 C18,60 50,44 90,44 C112,44 126,42 140,30 C150,22 160,20 168,20 C156,28 152,40 156,56 C162,70 164,82 162,96 C158,126 126,144 90,144 C50,144 18,126 18,96 Z" fill="url(#bubbleBlue)"/>
    <circle cx="28" cy="50" r="34" fill="var(--white)"/>
    <circle cx="28" cy="48" r="29" fill="var(--teal)"/>
    <path d="M17,35 c3,-2 6,-2 7,1 l3,6 c1,2 0,4 -2,5 l-2,1 c2,5 5,8 10,10 l1,-2 c1,-2 3,-3 5,-2 l6,3 c3,1 3,4 1,7 c-3,4 -8,5 -13,2 c-8,-4 -14,-10 -18,-18 c-2,-5 -1,-10 2,-13 z" fill="var(--white)"/>
  </svg>
  <div class="call-bubble__number">+233 30 781 6242</div>

  <div class="contact-card">
    <div class="contact-line">
      <svg width="24" height="18" viewBox="0 0 24 18"><rect width="24" height="18" rx="2" fill="var(--brand-blue)"/><path d="M2,3 L12,10 L22,3" stroke="var(--white)" stroke-width="2" fill="none"/></svg>
      <span>info@voloralaundry.example</span>
    </div>
    <div class="contact-line">
      <svg width="22" height="22" viewBox="0 0 22 22"><rect width="22" height="22" rx="3" fill="var(--brand-blue)"/></svg>
      <span>fb.com/voloralaundry</span>
    </div>
    <div class="contact-line">
      <svg width="22" height="24" viewBox="0 0 22 24"><path d="M11,24 C5,16 1,12 1,8 a10,10 0 0 1 20,0 c0,4 -4,8 -10,16 z" fill="var(--brand-blue)"/><circle cx="11" cy="8" r="3.5" fill="var(--white)"/></svg>
      <span>Kwentu-Dasor, Accra</span>
    </div>
  </div>

  <div class="hours-card">
    <div class="hours-card__panel">
      <div class="hours-card__open">OPEN</div>
      <div class="hours-card__times">
        <div class="hours-card__days">MON-SAT</div>
        <div class="hours-card__time">8:00 AM to 5:00 PM</div>
      </div>
    </div>
  </div>

  <svg class="laundry-art" viewBox="0 0 272 272" role="img" aria-label="Illustration of a red shirt washing in teal water with bubbles, inside a blue ring">
    <defs>
      <linearGradient id="ringBlue" x1="0" y1="0" x2="1" y2="1">
        <stop offset="0" stop-color="#2f78c4"/>
        <stop offset="1" stop-color="#80cdf1"/>
      </linearGradient>
      <linearGradient id="washTone" x1="0" y1="0" x2="0" y2="1">
        <stop offset="0" stop-color="#e8a89c"/>
        <stop offset=".5" stop-color="#7fcdb8"/>
        <stop offset="1" stop-color="#1dbb9c"/>
      </linearGradient>
    </defs>
    <circle cx="136" cy="136" r="128" fill="url(#ringBlue)"/>
    <circle cx="136" cy="136" r="106" fill="#eaf4fb"/>
    <circle cx="136" cy="136" r="94" fill="url(#washTone)"/>
  </svg>

  <div class="web-address">www.voloralaundry.example</div>
</section>

<section class="sticker">
  <div class="brand">
    <div class="brand__row"><span class="brand__dot"></span><span class="brand__name">volora</span></div>
    <div class="brand__sub">LAUNDRY AND DRY CLEANING</div>
    <div class="brand__slogan">Always Fresh &amp; Neat</div>
  </div>

  <div class="hours-card">
    <div class="hours-card__panel">
      <div class="hours-card__open">OPEN</div>
      <div class="hours-card__times">
        <div class="hours-card__days">MON-SAT</div>
        <div class="hours-card__time">8:00 AM to 5:00 PM</div>
      </div>
    </div>
  </div>

  <div class="contact-list">
    <div class="contact-line">
      <svg width="24" height="18" viewBox="0 0 24 18"><rect width="24" height="18" rx="2" fill="var(--brand-blue)"/><path d="M2,3 L12,10 L22,3" stroke="var(--white)" stroke-width="2" fill="none"/></svg>
      <span>info@voloralaundry.example</span>
    </div>
    <div class="contact-line">
      <svg width="22" height="22" viewBox="0 0 22 22"><rect width="22" height="22" rx="3" fill="var(--brand-blue)"/></svg>
      <span>fb.com/voloralaundry</span>
    </div>
    <div class="contact-line">
      <svg width="22" height="24" viewBox="0 0 22 24"><path d="M11,24 C5,16 1,12 1,8 a10,10 0 0 1 20,0 c0,4 -4,8 -10,16 z" fill="var(--brand-blue)"/><circle cx="11" cy="8" r="3.5" fill="var(--white)"/></svg>
      <span>Kwentu-Dasor, Accra</span>
    </div>
    <div class="contact-line">
      <svg width="22" height="22" viewBox="0 0 22 22"><path d="M4,2 c2,-1 4,-1 5,1 l2,4 c1,2 0,3 -1,4 l-1,1 c1,3 3,5 6,6 l1,-1 c1,-1 2,-2 4,-1 l3,2 c1,1 1,3 0,4 c-2,3 -6,3 -10,1 c-5,-3 -9,-7 -11,-12 c-1,-3 0,-7 2,-9 z" fill="var(--brand-blue)"/></svg>
      <span>+233 30 781 6242</span>
    </div>
  </div>

  <div class="web-address">www.voloralaundry.example</div>
</section>

</body>
</html>
```